Visitenkarten für ein Metallverarbeitsungsbetrieb
Zielgruppe
Metallverarbeitsungsbetrieb
spezialisiert auf Lasern
Aufgabenstellung
Passend zu unseren Logo und in den Farben, schlicht dennoch besonders

```html
<!DOCTYPE html>
<html lang="de">
<head>
<meta charset="utf-8">
<title>Nordbeck Laser GmbH – Visitenkarten</title>
<link rel="stylesheet" href="https://fonts.googleapis.com/css2?family=Barlow:wght@400;600;700&display=swap">
<style>
  :root {
    --page-bg: #e8e9ed;
    --navy-dark: #0a0f26;
    --navy-light: #1f1b34;
    --brand-blue: #1a86c4;
    --text-grey: #6b6b70;
    --card-white: #ffffff;
    --card-fade: #eef0f4;
  }
  * { margin: 0; padding: 0; box-sizing: border-box; }
  html, body { width: 1200px; height: 1200px; overflow: hidden; }
  body {
    background: var(--page-bg);
    font-family: "Barlow", Arial, sans-serif;
    display: flex;
    flex-direction: column;
    align-items: center;
    justify-content: center;
    gap: 60px;
  }
  .card {
    width: 760px;
    height: 460px;
    position: relative;
    box-shadow: 0 18px 40px rgba(0,0,0,0.18);
  }
  .card-front {
    background: linear-gradient(135deg, var(--navy-dark), var(--navy-light));
    display: flex;
    align-items: center;
    justify-content: center;
  }
  .brand {
    display: flex;
    align-items: center;
    gap: 22px;
  }
  .brand-dot {
    border: 8px solid var(--brand-blue);
    border-radius: 50%;
  }
  .card-front .brand-dot { width: 110px; height: 110px; }
  .card-front .brand-name {
    color: #ffffff;
    font-size: 44px;
    font-weight: 600;
    letter-spacing: 1px;
  }
  .card-back {
    background: linear-gradient(160deg, var(--card-white) 40%, var(--card-fade));
  }
  .card-back .brand {
    position: absolute;
    left: 60px;
    top: 60px;
    gap: 16px;
  }
  .card-back .brand-dot { width: 72px; height: 72px; border-width: 6px; }
  .card-back .brand-name {
    color: var(--text-grey);
    font-size: 26px;
    font-weight: 600;
  }
  .address {
    position: absolute;
    left: 60px;
    bottom: 60px;
    color: var(--text-grey);
    font-size: 24px;
    line-height: 1.25;
  }
  .address-company { font-weight: 700; }
  .contact-person {
    position: absolute;
    left: 430px;
    top: 75px;
  }
  .person-name {
    color: var(--brand-blue);
    font-weight: 700;
    font-size: 28px;
  }
  .person-role {
    color: var(--text-grey);
    font-size: 26px;
    letter-spacing: 1px;
  }
  .divider {
    position: absolute;
    left: 420px;
    top: 190px;
    width: 2px;
    height: 150px;
    background: linear-gradient(to bottom, rgba(26,134,196,0), var(--brand-blue), rgba(26,134,196,0));
  }
  .contact-details {
    position: absolute;
    left: 450px;
    top: 210px;
    color: var(--text-grey);
    font-size: 22px;
    line-height: 1.3;
    letter-spacing: 1px;
    list-style: none;
  }
</style>
</head>
<body>
  <section class="card card-front">
    <div class="brand">
      <span class="brand-dot"></span>
      <span class="brand-name">Nordbeck Laser GmbH</span>
    </div>
  </section>

  <section class="card card-back">
    <div class="brand">
      <span class="brand-dot"></span>
      <span class="brand-name">Nordbeck Laser GmbH</span>
    </div>

    <div class="contact-person">
      <p class="person-name">Jonas Feldmann</p>
      <p class="person-role">Geschäftsführer</p>
    </div>

    <span class="divider"></span>

    <ul class="contact-details">
      <li>+49 (2571) 480310</li>
      <li>info@nordbeck-laser.de</li>
      <li>www.nordbeck-laser.de</li>
    </ul>

    <address class="address">
      <span class="address-company">Nordbeck Laser GmbH</span><br>
      Lindenkamp 5<br>
      48291 Westerbeck
    </address>
  </section>
</body>
</html>
```